"MEET THE TEAM" page web design

We need a "meet the team" page for our website!
Please look at our website to see the style we need

We are looking for something unique, fun, cool, technology-style and yet professional. We plan on taking a picture of each employee (not sure if this will be a real photo/caricature/ black and white/goofy picture--> but we are open to any ideas you have that will work with the design) and putting it there, along with a little bio about each person.

Thanks! looking forward to working together:)
Updates

Project Deadline Extended
Reason: I am excited to see more designs and find the perfect fit. Thanks designers :)

Target Market(s)

People looking to purchase servers, workstations, components

Industry/Entity Type

Information Technology

Number of Pages Required

1 page

Font styles to use
Sans Serif
Other font styles liked:
• The font we use on our site so it matches

Requirements
Must have
• please look at our website qondimex.com and see the theme and colors we want.
• We have 13 employees but would like to have a design where we can add/remove people if we hire/terminate them without messing up the design.
• We are looking for something unique, fun, cool, technology-style and yet professional. We plan on taking a picture of each employee (not sure if this will be a real photo/caricature/ black and white/goofy picture--> but we are open to any ideas you have that will work with the design) and putting it there, along with a little bio about each person.
• We can upload anything you need
Nice to have
• We are also interested in having a design where when the cursor moves over a person then the bio comes out or moves around, or something. (This is not required, but we would love some cool ideas) And if you can come up with some design, we would have our programmers create it for us.
Should not have
• we are open to anything

```html
<!DOCTYPE html>
<html lang="en">
<head>
<meta charset="utf-8">
<title>About Us – Qondimex</title>
<link rel="stylesheet" href="https://fonts.googleapis.com/css2?family=Oswald:wght@300;400;500;600&display=swap">
<style>
:root{
  --teal:#2fb5a8;
  --teal-bright:#3cc8b9;
  --topbar:#36bcae;
  --ink:#2a2a2a;
  --muted:#444;
  --hero-a:#0b2e30;
  --hero-b:#1d5a58;
  --section-bg:#eeeeee;
  --card:#ffffff;
  --footer:#062522;
  --footer-bottom:#03110f;
  --white:#ffffff;
}
*{box-sizing:border-box;margin:0;padding:0}
html,body{width:1200px;height:2917px;overflow:hidden}
body{font-family:"Oswald",sans-serif;color:var(--ink);background:var(--white);position:relative}
a{color:inherit;text-decoration:none}

.top-bar{position:absolute;left:0;top:0;width:1200px;height:21px;background:var(--topbar);color:var(--white);font-size:11px;letter-spacing:.5px}
.top-bar .left{position:absolute;left:240px;top:3px;display:flex;gap:18px}
.top-bar .right{position:absolute;right:240px;top:3px;display:flex;gap:18px;font-weight:500}
.top-bar span{display:flex;align-items:center;gap:5px}
.top-bar svg{width:12px;height:12px;fill:var(--white)}

.site-header{position:absolute;left:0;top:21px;width:1200px;height:67px;background:var(--white)}
.brand{position:absolute;left:240px;top:16px;display:flex;align-items:center;gap:10px}
.brand-mark{width:34px;height:34px;border-radius:50%;background:var(--teal)}
.brand-name{font-size:28px;font-weight:500;color:var(--teal);letter-spacing:2px}
.search{position:absolute;left:735px;top:22px;width:224px;height:23px;border:1.5px solid var(--teal);border-radius:12px;font-size:12px;color:var(--teal);padding:2px 10px}
.search svg{position:absolute;right:8px;top:4px;width:13px;height:13px}

.main-nav{position:absolute;left:0;top:88px;width:1200px;height:29px;border-bottom:1px solid #ddd;background:var(--white)}
.main-nav ul{list-style:none;display:flex;position:absolute;left:240px;top:6px;font-size:11.5px;color:#333}
.main-nav li{padding:0 10px;border-left:1px solid #333;line-height:14px}
.main-nav li:first-child{padding-left:0;border-left:none}
.main-nav li.active{color:var(--teal)}

.hero{position:absolute;left:0;top:117px;width:1200px;height:321px;background:linear-gradient(90deg,var(--hero-a) 0%,#153f40 45%,var(--hero-b) 100%);border-bottom:3px solid var(--teal-bright);color:var(--white)}
.hero h1{position:absolute;left:248px;top:33px;font-size:34px;font-weight:500}
.hero .lead{position:absolute;left:248px;top:100px;width:700px;font-size:15px;font-weight:600;line-height:19px}
.hero .body{position:absolute;left:248px;top:168px;width:700px;font-size:11px;font-weight:500;line-height:19px}

.why{position:absolute;left:0;top:438px;width:1200px;height:324px;background:var(--white);border-bottom:3px solid var(--teal-bright)}
.section-title{font-size:33px;font-weight:500;color:var(--teal);text-align:center;letter-spacing:.5px}
.why .section-title{position:absolute;left:0;top:28px;width:1200px}
.feature{position:absolute;top:114px;width:180px;text-align:center}
.feature .ring{width:132px;height:132px;margin:0 auto;border-radius:50%;border:3px solid var(--teal);display:flex;align-items:center;justify-content:center}
.feature .ring .inner{width:112px;height:112px;border-radius:50%;border:2px solid var(--teal);display:flex;align-items:center;justify-content:center}
.feature svg{width:58px;height:58px;fill:var(--teal)}
.feature .label{margin-top:25px;font-size:17px;font-weight:500;color:#222}

.team{position:absolute;left:0;top:765px;width:1200px;height:1659px;background:var(--section-bg)}
.team .section-title{position:absolute;left:0;top:29px;width:1200px}
.team .intro{position:absolute;left:366px;top:98px;width:470px;font-size:11.5px;line-height:21px;color:#333;font-weight:400}

.card{position:absolute;width:346px;height:191px;background:var(--card)}
.card .avatar{position:absolute;left:8px;top:10px;width:90px;height:90px;border-radius:50%;border:2px solid var(--teal);padding:4px}
.card .avatar .photo{width:100%;height:100%;border-radius:50%;background:radial-gradient(circle at 50% 40%,#c9a48a,#6b5a4c)}
.card .name{position:absolute;left:121px;top:7px;font-size:18px;font-weight:500;color:#222}
.card .role{position:absolute;left:121px;top:32px;font-size:11px;color:#333}
.card .rule{position:absolute;left:121px;top:52px;width:40px;height:2px;background:var(--teal)}
.card .bio{position:absolute;left:121px;top:60px;width:214px;font-size:11.5px;line-height:22.5px;color:#333;font-weight:300}

.site-footer{position:absolute;left:0;top:2424px;width:1200px;height:435px;background:var(--footer);border-top:3px solid var(--teal-bright);color:var(--white)}
.footer-col{position:absolute;top:38px}
.footer-col h4{font-size:12px;font-weight:600;letter-spacing:.3px}
.quick-nav{left:247px}
.quick-nav ul{list-style:none;margin-top:30px;font-size:12px;line-height:22.5px;font-weight:500}
.about-col{left:426px;width:250px}
.about-col p{margin-top:30px;font-size:12px;line-height:22.5px;font-weight:500}
.contact-col{left:726px}
.contact-col .item{display:flex;gap:14px;font-size:12px;font-weight:500;line-height:17px;margin-top:30px}
.contact-col svg{width:14px;height:14px;fill:var(--white);flex:none;margin-top:2px}
.footer-rule{position:absolute;left:426px;top:337px;width:368px;height:1px;background:#24403d}
.social{position:absolute;left:498px;top:364px;display:flex;gap:27px}
.social span{width:14px;height:14px;border-radius:50%;background:var(--white);display:block}
.footer-bottom{position:absolute;left:0;top:2859px;width:1200px;height:58px;background:var(--footer-bottom);color:var(--white)}
.footer-bottom .mark{position:absolute;left:537px;top:20px;width:16px;height:16px;border-radius:50%;background:var(--white)}
.footer-bottom .copy{position:absolute;left:583px;top:14px;font-size:11px;line-height:14px;font-weight:600}
</style>
</head>
<body>

<div class="top-bar">
  <div class="left">
    <span><svg viewBox="0 0 24 24"><rect x="6" y="1" width="12" height="22" rx="2"/></svg>555-014-2290</span>
    <span><svg viewBox="0 0 24 24"><path d="M2 4h14v9H7l-4 4V4zm16 4h4v12l-4-3h-8v-2h8z"/></svg>LIVE CHAT</span>
    <span><svg viewBox="0 0 24 24"><path d="M1 3h4l3 12h12l3-9H7"/><circle cx="9" cy="20" r="2"/><circle cx="18" cy="20" r="2"/></svg>CART</span>
  </div>
  <div class="right">
    <span><svg viewBox="0 0 24 24"><path d="M2 10h12V5l8 7-8 7v-5H2z"/></svg>SIGN UP</span>
    <span><svg viewBox="0 0 24 24"><circle cx="12" cy="7" r="5"/><path d="M2 23c0-6 5-9 10-9s10 3 10 9z"/></svg>LOGIN</span>
  </div>
</div>

<header class="site-header">
  <div class="brand"><span class="brand-mark"></span><span class="brand-name">QONDIMEX</span></div>
  <div class="search">Search
    <svg viewBox="0 0 24 24" fill="none" stroke="#2fb5a8" stroke-width="3"><circle cx="10" cy="10" r="7"/><path d="M15 15l7 7"/></svg>
  </div>
</header>

<nav class="main-nav">
  <ul>
    <li>SERVERS</li><li>WORKSTATIONS</li><li>COMPONENTS</li><li>VIRTUAL REALITY</li><li>DRONES</li><li class="active">ABOUT US</li><li>BLOG</li><li>RESOURCES</li><li>CONTACT US</li>
  </ul>
</nav>

<section class="hero" role="img" aria-label="Engineer working in a server room">
  <h1>About Us</h1>
  <p class="lead">Qondimex, LLC provides Enterprise IT Hardware in the same quality of service and equipment that major brands provide without the major brand pricing.</p>
  <p class="body">We strive to deliver an alternate source for clients to obtain major brand hardware such as Delvane™, Harlix™, and Ibrem™ at discounted rates and faster response times. Because the core of Enterprise class equipment revolves around reliability, our on-site testing facility fully examines all equipment to ensure that all hardware shipped and received succeeds industry standards for quality control.</p>
</section>

<section class="why">
  <h2 class="section-title">Why Choose Us</h2>
  <div class="feature" style="left:241px">
    <div class="ring"><div class="inner"><svg viewBox="0 0 24 24"><path d="M2 3h13a2 2 0 0 1 2 2v6a2 2 0 0 1-2 2H7l-4 3v-3a2 2 0 0 1-1-2V5a2 2 0 0 1 2-2zm17 5h2a2 2 0 0 1 2 2v6a2 2 0 0 1-2 2v3l-4-3h-7a2 2 0 0 1-2-2v-1h7a3 3 0 0 0 3-3z"/></svg></div></div>
    <div class="label">Great Customer Service</div>
  </div>
  <div class="feature" style="left:420px">
    <div class="ring"><div class="inner"><svg viewBox="0 0 24 24"><path d="M14 1L4 14h7l-2 9 10-13h-7z"/></svg></div></div>
    <div class="label">Faster Turn-Around</div>
  </div>
  <div class="feature" style="left:599px">
    <div class="ring"><div class="inner"><svg viewBox="0 0 24 24"><path d="M6 2h12v3h4v3a5 5 0 0 1-5 5 6 6 0 0 1-4 3v3h4v3H7v-3h4v-3a6 6 0 0 1-4-3 5 5 0 0 1-5-5V5h4zm-2 5v1a3 3 0 0 0 2 3V7zm16 0h-2v4a3 3 0 0 0 2-3z"/></svg></div></div>
    <div class="label">5 Year Warranty</div>
  </div>
  <div class="feature" style="left:779px">
    <div class="ring"><div class="inner"><svg viewBox="0 0 24 24"><text x="12" y="20" text-anchor="middle" font-family="Oswald,sans-serif" font-size="22" font-weight="600">$</text></svg></div></div>
    <div class="label">Competitive Pricing</div>
  </div>
</section>

<section class="team">
  <h2 class="section-title">Our Dedicated Employees</h2>
  <p class="intro">Coupled with a 100,000 square foot warehouse, the amazing people of this team make it posible to provide countless configurations of Servers, Storages and Workstations to businesses worldwide within a 72 hours time-frame.</p>

  <article class="card" style="left:247px;top:202px">
    <div class="avatar"><div class="photo" role="img" aria-label="Portrait of Marta Lindqvist"></div></div>
    <h3 class="name">Marta Lindqvist</h3><div class="role">System Engineer</div><div class="rule"></div>
    <p class="bio">Leverage agile frameworks to provide a robust synopsis for high level overviews. Iterative approaches to corporate strategy foster collaborative thinking to further the overall value proposition.</p>
  </article>
  <article class="card" style="left:609px;top:202px">
    <div class="avatar"><div class="photo" role="img" aria-label="Portrait of Nkem Adeyemo"></div></div>
    <h3 class="name">Nkem Adeyemo</h3><div class="role">Technical Support</div><div class="rule"></div>
    <p class="bio">Bring to the table win-win survival strategies to ensure proactive domination. At the end of the day, going forward, a new normal that has evolved from generation X is on the runway heading towards a streamlined cloud solution.</p>
  </article>

  <article class="card" style="left:247px;top:406px">
    <div class="avatar"><div class="photo" role="img" aria-label="Portrait of Owen Hartley"></div></div>
    <h3 class="name">Owen Hartley</h3><div class="role">Support Representative</div><div class="rule"></div>
    <p class="bio">Capitalize on low hanging fruit to identify a ballpark value added activity to beta test. Override the digital divide with additional clickthroughs from DevOps. Nanotechnology immersion along the information.</p>
  </article>
  <article class="card" style="left:609px;top:406px">
    <div class="avatar"><div class="photo" role="img" aria-label="Portrait of Lucan Petrov"></div></div>
    <h3 class="name">Lucan Petrov</h3><div class="role">Area Sales Manager</div><div class="rule"></div>
    <p class="bio">Podcasting operational change management inside of workflows to establish a framework. Taking seamless key performance indicators offline to maximise the long tail. Keeping your eye on the ball while performing a deep dive.</p>
  </article>

  <article class="card" style="left:247px;top:610px">
    <div class="avatar"><div class="photo" role="img" aria-label="Portrait of Ilsa Brandwyn"></div></div>
    <h3 class="name">Ilsa Brandwyn</h3><div class="role">System Administrator</div><div class="rule"></div>
    <p class="bio">Collaboratively administrate empowered markets via plug-and-play networks. Dynamically procrastinate B2C users after installed base benefits. Dramatically visualize customer directed convergence.</p>
  </article>
  <article class="card" style="left:609px;top:610px">
    <div class="avatar"><div class="photo" role="img" aria-label="Portrait of Kerem Dufresne"></div></div>
    <h3 class="name">Kerem Dufresne</h3><div class="role">Web Developer</div><div class="rule"></div>
    <p class="bio">Efficiently unleash cross-media information without cross-media value. Quickly maximize timely deliverables for real-time schemas. Dramatically maintain clicks-and-mortar solutions without functional solutions.</p>
  </article>

  <article class="card" style="left:247px;top:816px">
    <div class="avatar"><div class="photo" role="img" aria-label="Portrait of Rosalie Quint"></div></div>
    <h3 class="name">Rosalie Quint</h3><div class="role">Customer Service</div><div class="rule"></div>
    <p class="bio">Completely synergize resource taxing relationships via premier niche markets. Professionally cultivate one-to-one customer service with robust ideas. Dynamically innovate resource-leveling customer service.</p>
  </article>
  <article class="card" style="left:609px;top:816px">
    <div class="avatar"><div class="photo" role="img" aria-label="Portrait of Noemi Castellan"></div></div>
    <h3 class="name">Noemi Castellan</h3><div class="role">Senior Systems Administrator</div><div class="rule"></div>
    <p class="bio">Objectively innovate empowered manufactured products whereas parallel platforms. Holisticly predominate extensible testing procedures for reliable supply chains. Dramatically engage top-line web services vis-a-vis cutting-edge.</p>
  </article>

  <article class="card" style="left:247px;top:1021px">
    <div class="avatar"><div class="photo" role="img" aria-label="Portrait of Ravi Vandermolen"></div></div>
    <h3 class="name">Ravi Vandermolen</h3><div class="role">Chief Technology Officer</div><div class="rule"></div>
    <p class="bio">Proactively envisioned multimedia based expertise and cross-media growth strategies. Seamlessly visualize quality intellectual capital without superior collaboration and idea-sharing.</p>
  </article>
  <article class="card" style="left:609px;top:1021px">
    <div class="avatar"><div class="photo" role="img" aria-label="Portrait of Aldric Moreno"></div></div>
    <h3 class="name">Aldric Moreno</h3><div class="role">Technical Support</div><div class="rule"></div>
    <p class="bio">Phosfluorescently engage worldwide methodologies with web-enabled technology. Interactively coordinate proactive e-commerce via process-centric "outside the box" thinking. Completely pursue scalable customer service.</p>
  </article>

  <article class="card" style="left:247px;top:1225px">
    <div class="avatar"><div class="photo" role="img" aria-label="Portrait of Priya Deshmane"></div></div>
    <h3 class="name">Priya Deshmane</h3><div class="role">Support Representative</div><div class="rule"></div>
    <p class="bio">Collaboratively administrate turnkey channels whereas virtual e-tailers. Objectively seize scalable metrics whereas proactive e-services. Seamlessly empower fully researched growth strategies.</p>
  </article>
  <article class="card" style="left:609px;top:1225px">
    <div class="avatar"><div class="photo" role="img" aria-label="Portrait of Theo Ambrose"></div></div>
    <h3 class="name">Theo Ambrose</h3><div class="role">Area Sales Manager</div><div class="rule"></div>
    <p class="bio">Credibly innovate granular internal or "organic" sources whereas high standards in web-readiness. Energistically scale future-proof core competencies vis-a-vis impactful experiences.</p>
  </article>

  <article class="card" style="left:247px;top:1429px">
    <div class="avatar"><div class="photo" role="img" aria-label="Portrait of Min-Seo Ferrante"></div></div>
    <h3 class="name">Min-Seo Ferrante</h3><div class="role">Support Representative</div><div class="rule"></div>
    <p class="bio">Synergistically evolve 2.0 technologies rather than just in time initiatives. Quickly deploy strategic networks with compelling e-business. Credibly pontificate highly efficient manufactured products and enabled data.</p>
  </article>
</section>

<footer class="site-footer">
  <div class="footer-col quick-nav">
    <h4>QUICK NAVIGATION</h4>
    <ul><li>Servers</li><li>Workstations</li><li>Components</li><li>Virtual Reality</li><li>Drones</li><li>About Us</li><li>Blog</li><li>Resources</li><li>Contact Us</li><li>Customer Support</li></ul>
  </div>
  <div class="footer-col about-col">
    <h4>ABOUT</h4>
    <p>Based in Westvale Park California, Qondimex offers custom servers, storage, and workstations for local businesses in Los Angeles, Beverly Hills, Thousand Oaks, Ventura, Orange County, Santa Barbara, Oxnard, Irvine, Anaheim, and San Diego. Qondimex also offers such products to clients throughout the United States and Worldwide.</p>
  </div>
  <div class="footer-col contact-col">
    <h4>CONTACT</h4>
    <div class="item"><svg viewBox="0 0 24 24"><path d="M12 1a8 8 0 0 0-8 8c0 6 8 14 8 14s8-8 8-14a8 8 0 0 0-8-8zm0 11a3 3 0 1 1 0-6 3 3 0 0 1 0 6z"/></svg><span>4120 Larkmoor Ave.<br>Westvale Park, CA 90210</span></div>
    <div class="item"><svg viewBox="0 0 24 24"><rect x="6" y="1" width="12" height="22" rx="2"/></svg><span>555-014-2290</span></div>
    <div class="item"><svg viewBox="0 0 24 24"><path d="M1 4h22v3l-11 7L1 7zm0 6l11 7 11-7v10H1z"/></svg><span>sales@qondimex.com</span></div>
  </div>
  <div class="footer-rule"></div>
  <div class="social" aria-label="Social links"><span></span><span></span><span></span><span></span></div>
</footer>

<div class="footer-bottom">
  <span class="mark"></span>
  <div class="copy">Qondimex, LLC.<br>Copyright © 2017</div>
</div>

</body>
</html>
```